Velmor Crest - Advanced Skincare and undetectable Makeup for Men

We are in need of a professional webpage for our company Velmor Crest. We help every man feel his best by looking his best. Inspired by the myth of Adonis, we offer makeup and skincare products along with education upon their use. Our mission is to celebrate masculinity in all of its forms, regardless of age, race, sexual orientation, or assigned gender at birth.

The webpage would serve as our online store, as a place where our clients can learn about our brand, view our "How-to" video tutorials, and get product information. An online blog will also be hosted in order to keep clients up to date with news, updates, media mentions, etc.

The color schemes that we use are mostly Black and Gold, with Red accents. please keep in mind that this is a men's cosmetics line, and therefore should read powerful, sexy, confident and bold - all with a high end look and feel.

Think along the lines of brands like Dirk Halvan, QBN, Belcuzzi, etc.

our logo is included in the files attached. images and copy will be added in at a later time; hence, general images that fit the feel and filler text is encouraged.

The products to be sold include:
a face cleanser in a pump dispenser bottle (1 size)
a mask in a round jar container (1 size)
a moisturizer in a pump container 1 size)
a concealer in a click pen with a brush applicator (3 shades)
a liquid liner pen (4 shades)
a contouring palette (2 shade options)
a setting spray (single option)

Target Market(s)

Millennial Men

Industry/Entity Type

Beauty

Number of Pages Required

5+ page

Font styles to use
Serif

Colors
ec1f27
000000
faa54b

Requirements
Must have
• ur essential requirements are:
• 1) a stunning and engaging landing page that truly captures the ideals of sexuality, boldness and confidence.
• 2) an interactive and engaging online store that is easy to update / add product / information to.
• 3) Product pages supporting various toggling images of the product, a shade selection option, ingredient information, usage instructions, pricing, and a link to a "how to video" unique to each individual product.
• 4) dedicated space where all of the tutorials can be organized together
• 5) an organized Blog section, that would include a segment for a Q&A section for us to update as the brand grows, ongoing contests (that would be easily hidden if there are no contests running at the moment) as well as general news and updates segment.
• 6) an "about us" page, where our customers are able to learn about our story, inspirations, humanitarian efforts and philosophies in product contents and purity.
• 7) a contact us page, which would include social media links, contact email and telephone number as well as physical address to be updated upon launch.
• 8) discrete privacy policy, terms of use, and return policy links available at the bottom of every page
Nice to have
• 1) A posting forum where clients could post their looks using our products, or maybe a live stream of our Pictoloop account.
• 2) a member sign in page so that we can collect and store customer information for faster check out, keep track of purchases attached to their email address (future loyalty program plans) and maintain an email database for email notifications and the such.

```html
<!DOCTYPE html>
<html lang="en">
<head>
<meta charset="utf-8">
<title>Velmor Crest</title>
<link href="https://fonts.googleapis.com/css2?family=Lora:wght@400;700&display=swap" rel="stylesheet">
<style>
:root{
  --navy:#0a0b1b;
  --ink:#05060f;
  --gold:#f2c431;
  --yellow:#f0c23a;
  --red:#d9262c;
  --white:#ffffff;
  --link:#2a4bd7;
  --skin:#b9825f;
  --skin-deep:#7a4c36;
  --hair:#2a1c14;
  --sky:#8fc0ec;
  --sea:#3aa9c6;
}
*{margin:0;padding:0;box-sizing:border-box}
html,body{width:1200px;height:1200px;overflow:hidden;background:#fff}
body{font-family:'Lora',Georgia,serif;position:relative}
.page{position:absolute;left:464px;top:0;width:339px;height:1500px;transform:scale(.8);transform-origin:0 0;background:var(--navy);overflow:hidden;color:var(--white)}
.abs{position:absolute}
.photo{position:absolute}
.h2{font-weight:700;color:var(--gold);font-size:13.5px;letter-spacing:.2px}
.tiny{font-size:3.1px;line-height:5.6px;color:var(--white)}
.btn{position:absolute;background:var(--red);color:#fff;border-radius:6px;font-size:3.4px;display:flex;align-items:center;justify-content:center;gap:3px}
.arrow{width:7px;height:4px}

/* header */
.header{left:0;top:0;width:339px;height:44px;background:var(--navy)}
.brand-mark{left:22px;top:8px;width:46px;text-align:center}
.brand-mark .dot{width:9px;height:9px;border:1.2px solid #fff;margin:0 auto 3px}
.brand-mark .name{font-size:3.3px;letter-spacing:1.4px}
.nav{left:154px;top:18px;display:flex;gap:9px;font-size:3.4px;font-weight:700}
.nav .active{position:relative}
.nav .active::after{content:"";position:absolute;left:0;right:0;top:7px;height:1px;background:var(--red)}
.icons{left:295px;top:17px;display:flex;gap:6px}

/* hero */
.hero-side{left:0;top:44px;width:57px;height:200px;background:linear-gradient(180deg,#3a4a64 0%,#1e2a42 35%,#16213a 60%,#2d3d58 80%,#4b5870 100%)}
.hero-main{left:57px;top:44px;width:282px;height:200px;background:linear-gradient(180deg,#7fb3e8 0%,#a9cdf2 30%,#5fc1d6 46%,#2b9fc0 54%,#bfe0ea 66%,#eef2f5 82%,#f7f7f8 100%)}
.hero-model{left:196px;top:44px;width:143px;height:200px;background:
  linear-gradient(90deg,rgba(185,130,95,0) 0%,rgba(185,130,95,.85) 22%,rgba(185,130,95,.95) 60%,rgba(140,95,70,.6) 100%),
  linear-gradient(180deg,var(--hair) 0%,var(--hair) 18%,var(--skin) 30%,var(--skin-deep) 62%,#f4f4f4 86%,#ffffff 100%);
  -webkit-mask-image:linear-gradient(90deg,transparent 0%,#000 25%);mask-image:linear-gradient(90deg,transparent 0%,#000 25%)}
.hero-arrow{left:6px;top:137px}
.tag-welcome{left:88px;top:121px;background:var(--yellow);color:#222;font-size:3.2px;padding:1px 3px}
.hero-title{left:88px;top:132px;background:var(--red);color:#fff;font-size:11.5px;padding:3px 7px 4px 2px;line-height:15px}

/* brand */
.brand-panel{left:0;top:244px;width:145px;height:139px;background:var(--navy)}
.brand-face{left:145px;top:244px;width:194px;height:246px;background:
  linear-gradient(180deg,rgba(30,20,15,.85) 0%,rgba(30,20,15,0) 14%,rgba(0,0,0,0) 75%,rgba(10,6,5,.6) 100%),
  linear-gradient(90deg,#c99274 0%,#b27a5c 28%,#6e4432 46%,#24150f 60%,#050505 78%,#000 100%)}
.brand-street{left:0;top:383px;width:145px;height:107px;background:
  linear-gradient(180deg,rgba(0,0,0,.15),rgba(0,0,0,.45)),
  linear-gradient(100deg,#2a1c12 0%,#4a3322 30%,#9b7240 55%,#d9ae6a 72%,#5a3d24 100%)}

/* how to */
.howto{left:0;top:490px;width:339px;height:195px;background:
  linear-gradient(90deg,rgba(0,0,0,.45) 0%,rgba(0,0,0,0) 40%,rgba(0,0,0,.2) 100%),
  linear-gradient(180deg,#3c3c3c 0%,#7a7a7a 28%,#5b5b5b 48%,#2e2e2e 70%,#141414 90%,#0c0c0c 100%)}
.thumb{left:258px;width:67px;height:45px;border:1.5px solid #eee}
.play{left:22px;top:637px}
.howto-title{left:60px;top:634px;font-size:8.5px;font-weight:700}
.howto-text{left:60px;top:648px;width:160px}

/* products */
.products-title{left:27px;top:720px}
.card{position:absolute;top:754px;width:113px}
.card .img{height:112px}
.card .title{margin-top:6px;color:var(--gold);font-size:9px;font-weight:700}
.card .desc{margin-top:2px;width:105px}
.card .price{position:absolute;top:150px;left:0;color:var(--red);font-size:10px}
.card .btn{top:153px;left:48px;width:56px;height:10px}
.progress{left:27px;top:955px;width:284px;height:4px;background:#fff;border-radius:2px}
.progress span{display:block;width:151px;height:4px;background:var(--yellow);border-radius:2px}

/* blog */
.blog-title{left:18px;top:1018px}
.blog-photo{left:113px;top:980px;width:226px;height:175px;background:
  linear-gradient(180deg,rgba(0,0,0,0) 45%,rgba(0,0,0,.7) 75%,#0b0b0b 100%),
  linear-gradient(100deg,#6c716a 0%,#a9a69d 25%,#8c6a55 45%,#b08a72 55%,#d8d4cc 75%,#9a978f 100%)}
.blog-side{left:0;top:1068px;width:113px;height:87px;background:linear-gradient(90deg,#6e1416 0%,#b02a2c 30%,#8a1c1f 55%,#c0393a 80%,#7a181b 100%);display:flex;align-items:center;justify-content:center;text-align:center;font-size:6.4px;font-weight:700;line-height:9px}
.featured{left:127px;top:1092px;background:var(--yellow);color:#222;font-size:5px;padding:1px 3px;font-weight:700}
.blog-copy{left:127px;top:1107px;font-size:6.3px;font-weight:700;line-height:10px;width:180px}
.read-more{left:127px;top:1133px;font-size:3.2px;color:var(--link);display:flex;gap:3px;align-items:center}

/* newsletter */
.news-photo{left:0;top:1175px;width:109px;height:130px;background:
  linear-gradient(90deg,rgba(0,0,0,0) 15%,rgba(140,95,70,.55) 40%,rgba(140,95,70,.55) 75%,rgba(0,0,0,0) 95%),
  linear-gradient(180deg,#7ab6e2 0%,#3f2a1e 14%,#b9825f 30%,#3aa9c6 55%,#b9825f 70%,#f2f2f2 88%,#ffffff 100%)}
.news-title{left:146px;top:1201px}
.news-sub{left:146px;top:1224px;font-size:8.4px;font-weight:700}
.news-text{left:146px;top:1242px;width:160px}
.news-input{left:146px;top:1268px;width:108px;height:13px;background:#fff;color:#555;font-size:3.4px;padding:4px 5px}
.news-btn{left:254px;top:1268px;width:52px;height:13px;border-radius:0}

/* footer */
.foot-art{left:0;top:1305px;width:170px;height:170px;background:
  linear-gradient(160deg,rgba(217,38,44,.35) 0%,rgba(0,0,0,0) 30%),
  linear-gradient(20deg,rgba(120,95,20,.45) 0%,rgba(0,0,0,0) 35%),
  linear-gradient(135deg,#141414 0%,#2b2521 50%,#0b0b0b 100%)}
.foot-brand{left:0;top:1372px;width:170px;text-align:center}
.foot-brand .sq{width:16px;height:16px;border:1.6px solid #fff;margin:0 auto 5px}
.foot-brand .name{font-size:4.6px;letter-spacing:2px}
.follow{left:170px;top:1326px;width:169px;text-align:center;color:var(--gold);font-size:6.2px;font-weight:700}
.socials{left:228px;top:1349px;display:flex;gap:3.5px}
.socials span{width:10px;height:10px;border-radius:50%}
.foot-info{left:170px;top:1384px;width:169px;height:91px;background:var(--yellow);color:#222}
.foot-info h4{font-size:5.2px;font-weight:700;position:absolute}
.foot-info .list{position:absolute;font-size:3px;line-height:6.4px}
.bottom{left:0;top:1475px;width:339px;height:25px;background:var(--ink);font-size:3.1px}
</style>
</head>
<body>
<div class="page">

  <header class="abs header">
    <div class="abs brand-mark"><div class="dot"></div><div class="name">VELMOR CREST</div></div>
    <nav class="abs nav">
      <span class="active">HOME</span><span>ABOUT US</span><span>SHOP</span><span>NEWS</span><span>BLOGS</span><span>CONTACT</span>
    </nav>
    <div class="abs icons">
      <svg width="7" height="7" viewBox="0 0 10 10"><circle cx="4" cy="4" r="3" fill="none" stroke="#fff" stroke-width="1.2"/><line x1="6.2" y1="6.2" x2="9" y2="9" stroke="#fff" stroke-width="1.2"/></svg>
      <svg width="7" height="7" viewBox="0 0 10 10"><path d="M0.5 1h1.5l1.3 5h5l1-3.5H3" fill="none" stroke="#fff" stroke-width="1"/><circle cx="4" cy="8.3" r=".8" fill="#fff"/><circle cx="7.5" cy="8.3" r=".8" fill="#fff"/></svg>
    </div>
  </header>

  <section class="hero">
    <div class="photo hero-side" role="img" aria-label="Man in navy shirt standing"></div>
    <div class="photo hero-main" role="img" aria-label="Beach and sea backdrop"></div>
    <div class="photo hero-model" role="img" aria-label="Portrait of a confident man in a white t-shirt"></div>
    <svg class="abs hero-arrow" width="14" height="14" viewBox="0 0 14 14"><path d="M9 2 L4 7 L9 12" fill="none" stroke="#fff" stroke-width="1.8"/></svg>
    <div class="abs tag-welcome">Welcome</div>
    <div class="abs hero-title">Velmor Crest</div>
  </section>

  <section class="brand">
    <div class="abs brand-panel"></div>
    <div class="photo brand-face" role="img" aria-label="Dramatic close-up of a man's face half in shadow"></div>
    <div class="photo brand-street" role="img" aria-label="Man in hat and checked shirt under warm lights"></div>
    <h2 class="abs h2" style="left:23px;top:276px">OUR BRAND</h2>
    <p class="abs tiny" style="left:23px;top:298px;width:102px">Uniquely disintermediate cross functional solutions and sticky strategic theme areas. Objectively myocardinate synergistic applications via a vis transparent partnerships. Assertively unleash bricks and clicks resources via transparent bandwidth.</p>
    <div class="btn" style="left:23px;top:341px;width:55px;height:10px">Explore More
      <svg class="arrow" viewBox="0 0 10 6"><path d="M0 3h9M6.5 .5 9 3 6.5 5.5" fill="none" stroke="#fff" stroke-width=".8"/></svg></div>
  </section>

  <section class="howto-block">
    <div class="photo howto" role="img" aria-label="Man in sunglasses seated on a deck chair, black and white"></div>
    <div class="photo thumb" style="top:508px;background:linear-gradient(90deg,#7a6a5a,#4a4442 50%,#8a7868)" role="img" aria-label="Tutorial thumbnail: man in grey suit"></div>
    <div class="photo thumb" style="top:561px;background:linear-gradient(90deg,#9ab2c2,#6a5a50 50%,#2c3640)" role="img" aria-label="Tutorial thumbnail: shirtless man"></div>
    <div class="photo thumb" style="top:614px;background:linear-gradient(90deg,#2f5e86,#8a6448 50%,#2a4a6a)" role="img" aria-label="Tutorial thumbnail: man in denim jacket"></div>
    <svg class="abs play" width="30" height="30" viewBox="0 0 30 30"><circle cx="15" cy="15" r="14" fill="none" stroke="#fff" stroke-width="1.3"/><path d="M12 9.5 L21 15 L12 20.5Z" fill="none" stroke="#fff" stroke-width="1.2"/></svg>
    <h3 class="abs howto-title">How To</h3>
    <p class="abs tiny howto-text">Uniquely disintermediate cross functional solutions and sticky strategic theme areas. Objectively myocardinate synergistic applications via a vis transparent partnerships. Assertively unleash bricks and clicks resources via transparent bandwidth.</p>
  </section>

  <section class="products">
    <h2 class="abs h2 products-title">OUR PRODUCTS</h2>

    <article class="card" style="left:27px">
      <div class="img" role="img" aria-label="Black and gold pump bottle of setting spray" style="background:linear-gradient(90deg,#f6f6f6 0%,#f6f6f6 22%,#c9a15a 28%,#1b1b1b 36%,#111 62%,#2a2a2a 70%,#efefef 82%,#fafafa 100%)"></div>
      <div class="title">Grunge Spray</div>
      <p class="tiny desc">Uniquely disintermediate cross functional solutions and sticky strategic theme areas.</p>
      <div class="price">$28</div>
      <div class="btn">Add to Cart <svg class="arrow" viewBox="0 0 10 6"><path d="M0 3h9M6.5 .5 9 3 6.5 5.5" fill="none" stroke="#fff" stroke-width=".8"/></svg></div>
    </article>

    <article class="card" style="left:147px">
      <div class="img" role="img" aria-label="Black liquid liner pen on white" style="background:linear-gradient(170deg,#f4f3f8 0%,#e6e4ec 44%,#2a2a2c 48%,#141414 51%,#dcdae2 55%,#f0eff4 100%)"></div>
      <div class="title">Grunge Spray</div>
      <p class="tiny desc">Uniquely disintermediate cross functional solutions and sticky strategic theme areas.</p>
      <div class="price">$28</div>
      <div class="btn">Add to Cart <svg class="arrow" viewBox="0 0 10 6"><path d="M0 3h9M6.5 .5 9 3 6.5 5.5" fill="none" stroke="#fff" stroke-width=".8"/></svg></div>
    </article>

    <article class="card" style="left:267px">
      <div class="img" role="img" aria-label="Contouring palette in black case" style="background:linear-gradient(160deg,#e6e6ea 0%,#c4c4ca 30%,#262628 40%,#1a1a1c 60%,#b88b5e 66%,#d8b489 75%,#2a2a2c 82%,#cfcfd4 100%)"></div>
      <div class="title">Grunge Spray</div>
      <p class="tiny desc">Uniquely disintermediate cross functional solutions and sticky strategic theme areas.</p>
      <div class="price">$28</div>
      <div class="btn" style="left:42px">Add to Cart <svg class="arrow" viewBox="0 0 10 6"><path d="M0 3h9M6.5 .5 9 3 6.5 5.5" fill="none" stroke="#fff" stroke-width=".8"/></svg></div>
    </article>

    <div class="abs progress"><span></span></div>
  </section>

  <section class="blog">
    <h2 class="abs h2 blog-title">OUR BLOG</h2>
    <div class="photo blog-photo" role="img" aria-label="Man lying down in a white shirt"></div>
    <div class="photo blog-side" role="img" aria-label="Red garments on a rail">Uniquely<br>disintermediate</div>
    <div class="abs featured">Featured</div>
    <p class="abs blog-copy">Uniquely disintermediate cross functional solutions and sticky strategic theme areas.</p>
    <div class="abs read-more">Read More <svg class="arrow" viewBox="0 0 10 6"><path d="M0 3h9M6.5 .5 9 3 6.5 5.5" fill="none" stroke="#2a4bd7" stroke-width=".8"/></svg></div>
  </section>

  <section class="newsletter">
    <div class="photo news-photo" role="img" aria-label="Portrait of a man at the seaside"></div>
    <h2 class="abs h2 news-title">NEWSLETTER</h2>
    <h3 class="abs news-sub">Subscribe To Our Mailing List</h3>
    <p class="abs tiny news-text">Uniquely disintermediate cross functional solutions and sticky strategic theme areas. Objectively myocardinate synergistic applications via a vis transparent</p>
    <div class="abs news-input">Email</div>
    <div class="btn news-btn">SUBSCRIBE</div>
  </section>

  <footer>
    <div class="photo foot-art" role="img" aria-label="Dark portrait of a man in sunglasses with scattered gold and red tiles"></div>
    <div class="abs foot-brand"><div class="sq"></div><div class="name">VELMOR CREST</div></div>
    <div class="abs follow">FOLLOW US ON</div>
    <div class="abs socials" aria-label="Social links">
      <span style="background:#d9262c" aria-label="Plusring"></span>
      <span style="background:#2f5bd3" aria-label="Facenook"></span>
      <span style="background:#f6e21a" aria-label="Snapwave"></span>
      <span style="background:#c33ab6" aria-label="Pictoloop"></span>
    </div>
    <div class="abs foot-info">
      <h4 style="left:26px;top:19px">Contact Info</h4>
      <div class="list" style="left:26px;top:33px">555-010-2244<br><br>48 HARLOW LANE<br>BROOKVALE, NV 89012<br><br>INFO@VELMORCREST.COM</div>
      <h4 style="left:100px;top:19px">Quick Links</h4>
      <div class="list" style="left:100px;top:33px">My Account<br>Shipping Info<br>Track Your Order<br>Delivery Info</div>
    </div>
    <div class="abs bottom">
      <span class="abs" style="left:5px;top:6px">Copyrights © 2017 All Rights Reserved</span>
      <span class="abs" style="left:258px;top:6px">Terms &amp; Condition &nbsp;&nbsp;&nbsp;|&nbsp;&nbsp;&nbsp; Privacy Policy</span>
    </div>
  </footer>

</div>
</body>
</html>
```